Need web redesign for cybersecurity startup whose mission is to make robust cybersecurity protection

We need a web redesign for Velundra, a cyber security startup. We already have a logo and website but we’re looking for a redesign to reflect the new messaging and positioning of the company – and to update our look with a more polished feel. We’re looking for clean, powerful, confident designs that easily communicate the problems within the cybersecurity space and how Velundra is the answer to those problems.

We can have the long-scrolling stripe layout for the home page, but we don’t want a bunch of interior pages with the same long-scroll format. We’d like to do something a little different and easier to navigate.

Velundra’s products simplify and automate cybersecurity defense so non-experts can successfully protect their information and focus on their business. Velundra’s mission is to provide proactive cybersecurity protection that is easy to use, easy to implement and easy to afford. The designs should reflect this populist message as well as confidence and maybe a little irreverence. Additional key words to describe the company are: secure, protection, easy, everyone.

Velundra offers multiple security products which can both be purchased directly from their site. They provide the world’s most widely used WAF rule set for Wardplex as well as Velundra Guarded Linux (VGL) and Velundra Guarded Linux Kernels to protect Linux servers, IoT devices and Podlane containers.

Target Market(s)

IT leaders in small and mid-sized businesses, hosting providers, and enterprise dev ops, product and security groups

Industry/Entity Type

Security

Number of Pages Required

5+ page

Font styles to use
Serif
Sans Serif

Requirements
Must have
• - We can have the long-scrolling stripe layout for the home page, but we don’t want a bunch of interior pages with the same long-scroll format. We’d like to do something a little different and easier to navigate.
• - Clean, powerful, confident designs
• - Real imagery coupled with line designs
Nice to have
• Specific icons to be used for all marketing and web materials for each product:
• - Velund Guarded for Linux (VG/L)
• - WardPlex Rules
• - Velundra Guarded Linux Kernels
• - KRIVE - Commercial Support
• - Guarded OS for Podlane
• - Guarded Apps for Podlane
Should not have
• - No typical imagery for cybersecurity such as binary code, hooded figures, etc.

```html
<!DOCTYPE html>
<html lang="en">
<head>
<meta charset="utf-8">
<title>Velundra — Harden Your Shell</title>
<link href="https://fonts.googleapis.com/css2?family=Montserrat:ital,wght@0,400;0,500;0,600;0,700;1,400&display=swap" rel="stylesheet">
<style>
  :root {
    --ink: #231f20;
    --body: #4a4544;
    --muted: #6b6665;
    --paper: #f9f6f3;
    --white: #ffffff;
    --red: #c8202f;
    --orange: #d9823a;
    --navy: #1b2f4f;
    --logo-grey: #9a9390;
  }
  * { box-sizing: border-box; margin: 0; padding: 0; }
  html, body { width: 1200px; height: 1200px; overflow: hidden; }
  body { font-family: "Montserrat", Arial, sans-serif; color: var(--ink); background: var(--paper); position: relative; }

  .partners {
    position: absolute; left: 0; top: 0; width: 1200px; height: 116px;
    background: linear-gradient(90deg, #5b6774 0%, #33475f 35%, #1c3558 70%, #14284a 100%);
  }
  .partner-card {
    position: absolute; top: 0; width: 165px; height: 70px; background: var(--white);
    display: flex; align-items: center; justify-content: center; gap: 8px;
    font-weight: 600; font-size: 16px; color: var(--logo-grey);
    box-shadow: 0 1px 3px rgba(0,0,0,.25);
  }
  .partner-card .dot { width: 12px; height: 12px; border-radius: 50%; background: var(--logo-grey); }

  .harden { position: absolute; left: 0; top: 116px; width: 1200px; height: 358px; background: var(--paper); }
  .harden h1 { position: absolute; left: 160px; top: 40px; font-size: 25px; font-weight: 700; letter-spacing: .3px; color: var(--ink); }
  .harden p { position: absolute; left: 160px; top: 74px; width: 335px; font-size: 12.5px; line-height: 19.5px; color: var(--body); }
  .btn {
    position: absolute; display: flex; align-items: center; justify-content: center;
    background: var(--red); color: var(--white); font-size: 12px; font-weight: 600; letter-spacing: .3px; height: 40px;
  }
  .harden .btn { left: 161px; top: 128px; width: 158px; }
  .video {
    position: absolute; left: 558px; top: 42px; width: 480px; height: 269px;
    border: 1px solid #d9d4d0;
    background: linear-gradient(180deg, #9a9590 0%, #7d7770 55%, #6a4a30 85%, #5a3c26 100%);
  }
  .video svg { position: absolute; left: 215px; top: 110px; }

  .testimonial {
    position: absolute; left: 0; top: 474px; width: 1200px; height: 376px;
    background: linear-gradient(90deg, #cfcfcd 0%, #8a8b8c 20%, #4c4e52 45%, #55575b 60%, #c9cac8 85%, #e8e9e6 100%);
  }
  .quote-card {
    position: absolute; left: 289px; top: 106px; width: 624px; height: 192px; background: var(--white);
    text-align: center;
  }
  .quote-mark {
    position: absolute; left: 289px; top: -23px; width: 46px; height: 46px; border-radius: 50%;
    background: var(--white); color: var(--orange); font-size: 30px; font-weight: 700; line-height: 56px;
  }
  .quote-card .company { margin-top: 30px; font-size: 22px; font-weight: 400; color: var(--ink); display: flex; justify-content: center; align-items: center; gap: 10px; }
  .quote-card .company .dot { width: 12px; height: 12px; border-radius: 50%; background: #7fb83a; }
  .quote-card blockquote { margin: 20px auto 0; width: 580px; font-size: 11.5px; line-height: 19.5px; font-style: italic; color: var(--body); }
  .quote-card .name { margin-top: 24px; font-size: 12px; font-weight: 600; color: var(--ink); }
  .quote-card .role { margin-top: 3px; font-size: 10.5px; color: var(--muted); }

  .containers { position: absolute; left: 0; top: 850px; width: 1200px; height: 350px; background: var(--paper); }
  .containers .art {
    position: absolute; left: 160px; top: 42px; width: 496px; height: 292px; border-radius: 10px;
    background: linear-gradient(160deg, #d7dadd 0%, #9aa3ab 40%, #2a3340 65%, #1f9fd0 100%);
  }
  .containers h2 { position: absolute; left: 686px; top: 42px; font-size: 24px; line-height: 26px; font-weight: 700; color: var(--ink); }
  .containers h2 .yes { color: var(--orange); }
  .containers p { position: absolute; left: 686px; top: 101px; width: 360px; font-size: 12.5px; line-height: 19.5px; color: var(--body); }
  .containers .btn { left: 686px; top: 255px; width: 121px; }
</style>
</head>
<body>
  <header class="partners" role="img" aria-label="Photo of a hand in a dark suit sleeve on a blue background">
    <div class="partner-card" style="left:164px">Brevanth</div>
    <div class="partner-card" style="left:341px">Quelm</div>
    <div class="partner-card" style="left:518px;font-size:14px">Harbour Lantern</div>
    <div class="partner-card" style="left:696px">Ironvale</div>
    <div class="partner-card" style="left:873px"><span class="dot"></span>Pathmere</div>
  </header>

  <section class="harden">
    <h1>HARDEN YOUR SHELL NOW!</h1>
    <p>It's real security, where you need it, and at a price you can afford.</p>
    <a class="btn">GET STARTED NOW</a>
    <div class="video" role="img" aria-label="Video still of a spokesperson at an office desk with a cat and a desk lamp">
      <svg width="50" height="50" viewBox="0 0 50 50" aria-hidden="true">
        <circle cx="25" cy="25" r="23" fill="rgba(0,0,0,.15)" stroke="#fff" stroke-width="2"/>
        <path d="M19 14 L35 25 L19 36 Z" fill="#fff"/>
      </svg>
    </div>
  </section>

  <section class="testimonial" role="img" aria-label="Photo of a smiling professional in a suit in an office">
    <div class="quote-card">
      <div class="quote-mark">&ldquo;</div>
      <div class="company">TESSEL GECKO <span class="dot"></span></div>
      <blockquote>&ldquo;We trust our server security to Velundra Guarded Linux because it works. We've used it for years and it has been essential in keeping dark forces at bay.&rdquo;</blockquote>
      <div class="name">Adrian Kellow</div>
      <div class="role">Tessel Gecko</div>
    </div>
  </section>

  <section class="containers">
    <div class="art" role="img" aria-label="Illustration of a laptop showing a tablet with app icons and a whale carrying shipping containers"></div>
    <h2><span class="yes">YES.</span> YOU CAN SECURE<br>PODLANE CONTAINERS</h2>
    <p>Podlane is the fastest growing application developer software in the world. But, people don't realize that their containers are wide open to cyber attacks. Velundra provides a secure OS kernel that is inherited by all containers on a single server. It's easy to install, doesn't impact performance and protects your containers against malicious attacks immediately.</p>
    <a class="btn">LEARN MORE</a>
  </section>
</body>
</html>
```